Business Cards

I'd like help creating business cards with the full logo "Veltrona Capital Partners" on the back of the card (navy background with white writing), and abbreviated logo "VCP" on the front. Would like to list name, title, phone number, email, and website listed on front of card. Would like to keep very simple. Front font Arial or similar.

```html
<!DOCTYPE html>
<html lang="en">
<head>
<meta charset="utf-8">
<title>Veltrona Capital Partners – Business Cards</title>
<link href="https://fonts.googleapis.com/css2?family=Arimo:wght@400;700&display=swap" rel="stylesheet">
<style>
  :root {
    --backdrop: #222222;
    --navy: #1f3a75;
    --navy-deep: #1b3368;
    --paper: #ffffff;
    --ink: #111111;
    --rule: #1a1a1a;
  }
  * { box-sizing: border-box; margin: 0; padding: 0; }
  html, body {
    width: 1200px; height: 780px; overflow: hidden;
    background: var(--backdrop);
    font-family: "Arimo", Arial, sans-serif;
  }
  .canvas {
    position: relative; width: 1200px; height: 780px;
    display: flex; align-items: center; justify-content: center; gap: 44px;
  }
  .card {
    position: relative; width: 520px; height: 300px; overflow: hidden;
    box-shadow: 0 12px 30px rgba(0,0,0,.5);
  }
  /* Front */
  .card-front { background: var(--paper); }
  .front-band { position: absolute; left: 0; bottom: 0; width: 520px; height: 26px; }
  .monogram {
    position: absolute; left: 34px; top: 92px;
    font-weight: 700; font-size: 74px; letter-spacing: 2px; color: var(--navy);
  }
  .divider {
    position: absolute; left: 238px; top: 52px; width: 1px; height: 190px;
    background: var(--rule);
  }
  .identity { position: absolute; left: 262px; top: 64px; }
  .person-name { font-weight: 700; font-size: 30px; color: var(--navy); line-height: 1.1; }
  .person-title { font-size: 14px; color: var(--ink); margin-top: 6px; }
  .contact-list { list-style: none; margin-top: 26px; }
  .contact-item {
    display: flex; align-items: center; gap: 8px;
    font-size: 14px; color: var(--ink); line-height: 1.6;
  }
  .contact-icon { width: 13px; height: 13px; flex: none; }
  /* Back */
  .card-back { background: var(--navy); }
  .back-texture { position: absolute; inset: 0; background: linear-gradient(135deg, var(--navy) 0%, var(--navy-deep) 100%); }
  .back-wordmark {
    position: absolute; left: 50%; top: 50%; transform: translate(-50%, -50%);
    font-weight: 700; font-size: 22px; letter-spacing: 1px; color: var(--paper);
    white-space: nowrap;
  }
</style>
</head>
<body>
<main class="canvas">
  <section class="card card-front" aria-label="Business card front">
    <svg class="front-band" viewBox="0 0 520 26" aria-hidden="true">
      <polygon points="0,0 150,0 140,14 520,14 520,26 0,26" fill="var(--navy)"/>
    </svg>
    <div class="monogram">VCP</div>
    <div class="divider"></div>
    <div class="identity">
      <h1 class="person-name">Dana Holloway</h1>
      <p class="person-title">Co-Founder and Managing Partner</p>
      <ul class="contact-list">
        <li class="contact-item">
          <svg class="contact-icon" viewBox="0 0 16 16" aria-hidden="true"><path d="M3 1h3l1.5 4-2 1.3a9 9 0 0 0 4.2 4.2L11 8.5l4 1.5v3a2 2 0 0 1-2 2A12 12 0 0 1 1 3a2 2 0 0 1 2-2z" fill="var(--navy)"/></svg>
          (555) 014-2290
        </li>
        <li class="contact-item">
          <svg class="contact-icon" viewBox="0 0 16 16" aria-hidden="true"><circle cx="8" cy="8" r="6.5" fill="none" stroke="var(--navy)" stroke-width="1.6"/><path d="M1.5 8h13M8 1.5c-3 3.5-3 9.5 0 13M8 1.5c3 3.5 3 9.5 0 13" fill="none" stroke="var(--navy)" stroke-width="1.2"/></svg>
          www.veltronacp.com
        </li>
        <li class="contact-item">
          <svg class="contact-icon" viewBox="0 0 16 16" aria-hidden="true"><rect x="1" y="3" width="14" height="10" rx="1" fill="var(--navy)"/><path d="M1.5 3.5 8 9l6.5-5.5" fill="none" stroke="#fff" stroke-width="1.3"/></svg>
          Dana.Holloway@VeltronaCP.com
        </li>
      </ul>
    </div>
  </section>

  <section class="card card-back" aria-label="Business card back">
    <div class="back-texture" role="img" aria-label="Tone-on-tone navy pattern of repeated company name"></div>
    <div class="back-wordmark">Veltrona Capital Partners</div>
  </section>
</main>
</body>
</html>
```